New Shop front sign with 2 x window sign designs

I require a New shop sign for a retail store. with 2 x window design for printing onto diabond material. it must be bright and fresh. please see images of sizes required.
Updates

Please see a similar logo for the top sign, it shows Vantro. but we require the same or similar (better) design saying Plum stall. It will be on a plain backgroung of white, with the slogan at the bottom most items below £1. and also a seperate area for the "small family owned business" I just want a plain simple top sign that is professional and stylish. please see the upload area wher i have added the vantro logo. i look forward to your designs coming through to me,

Target Market(s)

This is for a retail store, and it needs to reflect our cheap prices.

Industry/Entity Type

Retail

Requirements
Must have
• For the top sign, it must say "The Plum Stall" in bigger text as the main sign. and under the main words, we need to have a slogan similar to "Big Brands Better Prices - Most products under £1"
• Also on the top sign, I would like to add "local family run business"
• The backround needs to reflect cheap prices, maybe like £ signs and good artwork.
• The first window sign, needs to be about our cheap mr quandle ice cream, where it will be sold for 89p. it must have a cornet cone with soft icecream top. with good artwork, advertising the low price of only 99p.
• The second window needs to advertise our slush, small slush 89p - Large £1.39 - Yard Cup £1.99
• Please see attached similar artwork on my previous tasks.
Nice to have
• It is nice to have a full bright design that will invite customers to my store whilst walking past
Should not have
• I do not require a basic design, this must be top of the range professional crisp and clean.

```html
<!DOCTYPE html>
<html lang="en">
<head>
<meta charset="utf-8">
<title>Ice Cream Window Sign</title>
<link rel="stylesheet" href="https://fonts.googleapis.com/css2?family=Pacifico&family=Montserrat:wght@400;800&family=Oswald:wght@700&display=swap">
<style>
  :root {
    --backdrop: #e4e5e5;
    --sky-deep: #0fb2d1;
    --sky-mid: #5fd3e6;
    --sky-light: #e6fbfe;
    --title-pink: #f0468f;
    --title-deep: #e0307c;
    --title-white: #ffffff;
    --ribbon-dark: #b3141c;
    --ribbon-red: #e0281f;
    --ribbon-orange: #f0501c;
    --ribbon-fold: #7d0d12;
    --badge-top: #f3801c;
    --badge-bottom: #e0341a;
    --treat-pink: #ee7fb4;
    --treat-cone: #e2b47a;
  }
  html, body {
    margin: 0;
    width: 980px;
    height: 1200px;
    overflow: hidden;
    background: var(--backdrop);
  }
  .canvas {
    position: relative;
    width: 980px;
    height: 1200px;
  }
  .window-sign {
    position: absolute;
    left: 225px;
    top: 40px;
    width: 530px;
    height: 1120px;
    display: block;
  }
  .title-text {
    font-family: 'Pacifico', cursive;
    fill: var(--title-white);
    stroke: var(--title-pink);
    stroke-width: 26px;
    stroke-linejoin: round;
    paint-order: stroke fill;
  }
  .title-shadow {
    font-family: 'Pacifico', cursive;
    fill: var(--title-deep);
    stroke: var(--title-deep);
    stroke-width: 26px;
    stroke-linejoin: round;
  }
  .ribbon-small {
    font-family: 'Montserrat', sans-serif;
    font-weight: 400;
    fill: #ffffff;
  }
  .ribbon-main {
    font-family: 'Montserrat', sans-serif;
    font-weight: 800;
    fill: #ffffff;
  }
  .price-text {
    font-family: 'Oswald', sans-serif;
    font-weight: 700;
    fill: #ffffff;
  }
</style>
</head>
<body>
<div class="canvas">
  <svg class="window-sign" viewBox="0 0 776 1640" xmlns="http://www.w3.org/2000/svg">
    <defs>
      <linearGradient id="sky" x1="0" y1="0" x2="1" y2="0">
        <stop offset="0" stop-color="var(--sky-deep)"/>
        <stop offset="0.5" stop-color="var(--sky-mid)"/>
        <stop offset="1" stop-color="var(--sky-deep)"/>
      </linearGradient>
      <radialGradient id="glow" cx="0.5" cy="0.5" r="0.5">
        <stop offset="0" stop-color="#ffffff" stop-opacity="0.95"/>
        <stop offset="0.45" stop-color="var(--sky-light)" stop-opacity="0.55"/>
        <stop offset="1" stop-color="var(--sky-light)" stop-opacity="0"/>
      </radialGradient>
      <linearGradient id="treat" x1="0" y1="0" x2="0" y2="1">
        <stop offset="0" stop-color="var(--treat-pink)" stop-opacity="0.85"/>
        <stop offset="0.5" stop-color="#f2a6b8" stop-opacity="0.7"/>
        <stop offset="1" stop-color="var(--treat-cone)" stop-opacity="0.55"/>
      </linearGradient>
      <linearGradient id="ribbon" x1="0" y1="0" x2="1" y2="0">
        <stop offset="0" stop-color="var(--ribbon-dark)"/>
        <stop offset="0.5" stop-color="var(--ribbon-red)"/>
        <stop offset="1" stop-color="var(--ribbon-orange)"/>
      </linearGradient>
      <linearGradient id="badge" x1="0" y1="0" x2="1" y2="1">
        <stop offset="0" stop-color="var(--badge-top)"/>
        <stop offset="1" stop-color="var(--badge-bottom)"/>
      </linearGradient>
    </defs>

    <rect class="sky" width="776" height="1640" fill="url(#sky)"/>
    <ellipse class="sky-glow" cx="388" cy="760" rx="480" ry="620" fill="url(#glow)"/>

    <g class="title">
      <text class="title-shadow" x="455" y="268" font-size="170" text-anchor="middle" textLength="360" lengthAdjust="spacingAndGlyphs">Ice</text>
      <text class="title-text" x="452" y="262" font-size="170" text-anchor="middle" textLength="360" lengthAdjust="spacingAndGlyphs">Ice</text>
      <text class="title-shadow" x="395" y="392" font-size="170" text-anchor="middle" textLength="660" lengthAdjust="spacingAndGlyphs">Cream</text>
      <text class="title-text" x="392" y="386" font-size="170" text-anchor="middle" textLength="660" lengthAdjust="spacingAndGlyphs">Cream</text>
    </g>

    <rect class="cones-artwork" x="120" y="540" width="510" height="700" rx="60" fill="url(#treat)" role="img" aria-label="Three swirled soft-serve ice cream cones in chocolate, strawberry and lemon on wafer cones"/>

    <g class="ribbon-banner">
      <polygon class="ribbon-fold" points="130,925 170,918 170,1000 130,1000" fill="var(--ribbon-fold)" opacity="0"/>
      <polygon class="ribbon-best" points="130,925 625,842 625,905 130,988" fill="url(#ribbon)"/>
      <polygon class="ribbon-collection" points="155,1185 670,1105 670,1165 155,1245" fill="url(#ribbon)"/>
      <polygon class="ribbon-flavour" points="27,1057 750,907 750,1022 27,1167" fill="url(#ribbon)"/>

      <text class="ribbon-small" x="380" y="930" font-size="54" text-anchor="middle" letter-spacing="12" transform="rotate(-9.5 380 912)">BEST</text>
      <text class="ribbon-main" x="390" y="1068" font-size="96" text-anchor="middle" textLength="540" lengthAdjust="spacing" transform="rotate(-11.7 390 1035)">FLAVOUR</text>
      <text class="ribbon-main" x="68" y="1108" font-size="44" text-anchor="middle" transform="rotate(-11.7 68 1093)">★</text>
      <text class="ribbon-main" x="712" y="975" font-size="44" text-anchor="middle" transform="rotate(-11.7 712 960)">★</text>
      <text class="ribbon-small" x="412" y="1192" font-size="44" text-anchor="middle" letter-spacing="4" transform="rotate(-8.8 412 1175)">COLLECTION</text>
    </g>

    <g class="price-badge" transform="translate(422 1364)">
      <g class="badge-outline" fill="#ffffff">
        <rect x="-98" y="-98" width="196" height="196"/>
        <rect x="-98" y="-98" width="196" height="196" transform="rotate(15)"/>
        <rect x="-98" y="-98" width="196" height="196" transform="rotate(30)"/>
        <rect x="-98" y="-98" width="196" height="196" transform="rotate(45)"/>
        <rect x="-98" y="-98" width="196" height="196" transform="rotate(60)"/>
        <rect x="-98" y="-98" width="196" height="196" transform="rotate(75)"/>
      </g>
      <g class="badge-fill" fill="url(#badge)">
        <rect x="-91" y="-91" width="182" height="182"/>
        <rect x="-91" y="-91" width="182" height="182" transform="rotate(15)"/>
        <rect x="-91" y="-91" width="182" height="182" transform="rotate(30)"/>
        <rect x="-91" y="-91" width="182" height="182" transform="rotate(45)"/>
        <rect x="-91" y="-91" width="182" height="182" transform="rotate(60)"/>
        <rect x="-91" y="-91" width="182" height="182" transform="rotate(75)"/>
      </g>
      <text class="price-text" x="-2" y="52" font-size="148" text-anchor="middle">89</text>
      <text class="price-text" x="100" y="58" font-size="54" text-anchor="middle">p</text>
    </g>
  </svg>
</div>
</body>
</html>
```